Business Card Design Project

We are rebranding an existing automotive collision repair business. The business is called dentworks garage. I have attached logo but I'm not tied to that. I want to leave this wide open.

I want this card to say we are professional, competent, cutting edge. We are focused on customers and use a lot of the latest technology to make the customer experience different. We sign customers in on iPads. Paperwork I signed electronically and updates are sent via text, email, logging on a website or as they wish. I want this innovation and image to come through in our cards

Target Market(s)

60%. Women 40% men. Age 35-60

Industry/Entity Type

Automotive

Requirements
Must have
• The card must have name, title, phone,email, cell, web page

```html
<!DOCTYPE html>
<html lang="en">
<head>
<meta charset="utf-8">
<title>Dentworks Garage — Business Card</title>
<link href="https://fonts.googleapis.com/css2?family=Source+Sans+3:wght@400;600;700&display=swap" rel="stylesheet">
<style>
  :root {
    --bg: #e4e4e6;
    --green-light: #8cc63f;
    --green: #76b532;
    --green-dark: #5ea52e;
    --white: #ffffff;
    --paper: #f2f2f3;
    --grey-rule: #c9c9cc;
    --text-soft: #e8f4d8;
  }
  * { box-sizing: border-box; margin: 0; padding: 0; }
  html, body { width: 883px; height: 1200px; overflow: hidden; }
  body {
    background: var(--bg);
    font-family: "Source Sans 3", "Helvetica Neue", Arial, sans-serif;
    position: relative;
  }
  .card {
    position: absolute;
    left: 161px;
    width: 560px;
    height: 320px;
    overflow: hidden;
    box-shadow: 0 6px 18px rgba(0,0,0,0.18);
  }
  .card--front {
    top: 190px;
    background: linear-gradient(135deg, var(--green-light) 0%, var(--green) 55%, var(--green-dark) 100%);
    color: var(--white);
    text-align: center;
  }
  .front-brand {
    position: absolute;
    top: 118px;
    left: 0; right: 0;
    font-weight: 700;
    font-size: 44px;
    letter-spacing: 0.5px;
  }
  .front-web {
    position: absolute;
    top: 228px;
    left: 0; right: 0;
    font-size: 16px;
  }
  .card--back {
    top: 640px;
    background: var(--paper);
  }
  .back-wave { position: absolute; inset: 0; }
  .back-brand {
    position: absolute;
    top: 40px;
    right: 40px;
    font-weight: 700;
    font-size: 32px;
    color: var(--green);
  }
  .holder {
    position: absolute;
    left: 36px;
    top: 176px;
    color: var(--white);
  }
  .holder-name { font-weight: 600; font-size: 21px; }
  .holder-title { font-size: 16px; color: var(--text-soft); }
  .contacts {
    position: absolute;
    left: 318px;
    top: 170px;
    list-style: none;
    color: var(--white);
    font-size: 16px;
    line-height: 24px;
  }
  .contacts li { display: flex; align-items: center; gap: 8px; }
  .contacts svg { width: 12px; height: 12px; fill: var(--white); flex: none; }
</style>
</head>
<body>
  <section class="card card--front" aria-label="Card front">
    <div class="front-brand">Dentworks Garage</div>
    <div class="front-web">www.dentworksgarage.com</div>
  </section>

  <section class="card card--back" aria-label="Card back">
    <svg class="back-wave" viewBox="0 0 560 320" preserveAspectRatio="none" aria-hidden="true">
      <defs>
        <linearGradient id="backGreen" x1="0" y1="0" x2="1" y2="1">
          <stop offset="0" stop-color="#8cc63f"/>
          <stop offset="1" stop-color="#6fb232"/>
        </linearGradient>
      </defs>
      <path d="M0 62 C120 50 220 70 330 118 C420 156 500 146 560 140 L560 320 L0 320 Z" fill="#b9dd8c"/>
      <path d="M0 70 C120 58 220 80 330 128 C420 166 500 156 560 150 L560 320 L0 320 Z" fill="url(#backGreen)"/>
    </svg>
    <div class="back-brand">Dentworks Garage</div>
    <div class="holder">
      <div class="holder-name">Liam Carter</div>
      <div class="holder-title">Managing Director</div>
    </div>
    <ul class="contacts">
      <li><svg viewBox="0 0 12 12"><path d="M2.5 0.8l2 2.4-1 1.2c.7 1.5 1.8 2.6 3.3 3.3l1.2-1 2.4 2-1 2.3C5 10.6 1.4 7 0.2 1.8z"/></svg>555.0142.3380</li>
      <li><svg viewBox="0 0 12 12"><path d="M3 0h6v12H3zM4 1.5v8h4v-8z"/></svg>555.0142.3381</li>
      <li><svg viewBox="0 0 12 12"><path d="M3 0h6v3H3zM0 4h12v6h-2v2H2v-2H0zM3 8v3h6V8z"/></svg>555.0142.3382</li>
      <li><svg viewBox="0 0 12 12"><path d="M0 2h12v1L6 7 0 3zM0 4.5l6 4 6-4V10H0z"/></svg>info@dentworksgarage.com</li>
      <li><svg viewBox="0 0 12 12"><path d="M6 0a6 6 0 100 12A6 6 0 006 0zm0 1.2c.8 0 1.6 1.9 1.7 4.2H4.3C4.4 3.1 5.2 1.2 6 1.2zM4.3 6.6h3.4c-.1 2.3-.9 4.2-1.7 4.2s-1.6-1.9-1.7-4.2z"/></svg>www.dentworksgarage.com</li>
    </ul>
  </section>
</body>
</html>
```